Asia Hotel need a card and logo

The new hotel in East Asia, Taiwan need a business card and logo design.The hotel's Chinese name is 岚溪文旅,English name is "Virel Hotel".The core concept of this hotel is "Eco green", going to use many plant etc.,The building's first outlook draft is attached in the file for your reference.The style be modern and fashion will be good. Thank you.
Target Market(s)
East Asia
Industry/Entity Type
Hotel
Contact Information for Business Card
The hotel's name both in Chinese and English :岚溪商旅 Virel Hotel
The logo, address, E-mail and tel number place.
Stuff's name and title.
Font styles to use
Colors
Designer to choose colors to be used in the design.
Look and feel
Each slider illustrates characteristics of the customer's brand and the style your logo design should communicate.

```html
<!DOCTYPE html>
<html lang="en">
<head>
<meta charset="utf-8">
<title>Virel Hotel – Business Card &amp; Identity</title>
<link rel="stylesheet" href="https://fonts.googleapis.com/css2?family=Arimo:wght@400&family=Noto+Sans+TC:wght@400;500&display=swap">
<style>
  :root {
    --purple: #55308f;
    --purple-light: #7a5ab0;
    --purple-ink: #4a2a8a;
    --lime: #a9c73e;
    --lime-bg: #b1cf4a;
    --lime-pale: #e4efc6;
    --paper: #ffffff;
    --mist: #e6e7ec;
    --ink: #333333;
    --icon: #555555;
    --name-font: "Noto Sans TC", "Arimo", sans-serif;
    --text-font: "Arimo", "Noto Sans TC", sans-serif;
  }
  * { box-sizing: border-box; margin: 0; padding: 0; }
  html, body { width: 848px; height: 1200px; overflow: hidden; }
  body { position: relative; font-family: var(--text-font); background: var(--paper); }

  .stage-top { position: absolute; left: 0; top: 0; width: 848px; height: 490px; background: var(--lime-bg); }
  .stage-cards { position: absolute; left: 0; top: 490px; width: 848px; height: 400px; background: var(--mist); }
  .panel { position: absolute; top: 890px; width: 424px; height: 310px; }
  .panel--light { left: 0; background: var(--paper); }
  .panel--dark { left: 424px; background: var(--purple); }

  .card { position: absolute; width: 312px; height: 192px; overflow: hidden;
          box-shadow: 0 10px 22px rgba(40, 40, 60, 0.18); }
  .card--front { background: var(--purple); }
  .card--back { background: var(--paper); }

  .card__texture { position: absolute; inset: 0;
    background:
      radial-gradient(ellipse 70px 120px at 18px 130px, rgba(122, 90, 176, 0.55), transparent 70%),
      radial-gradient(ellipse 80px 130px at 296px 70px, rgba(122, 90, 176, 0.55), transparent 70%),
      radial-gradient(ellipse 40px 50px at 70px 192px, rgba(122, 90, 176, 0.4), transparent 70%); }
  .card__leaf { position: absolute; left: 0; top: 0; width: 312px; height: 192px; }

  .brand { position: absolute; text-align: center; color: var(--lime); font-family: var(--name-font); }
  .brand__mark { display: block; margin: 0 auto; border-radius: 50%; background: var(--lime); }
  .brand__cn { display: block; font-weight: 500; letter-spacing: 1px; }
  .brand__en { display: block; font-family: var(--text-font); }

  .card .brand { width: 120px; top: 55px; }
  .card .brand__mark { width: 34px; height: 34px; margin-bottom: 30px; }
  .card .brand__cn { font-size: 10px; line-height: 14px; }
  .card .brand__en { font-size: 10px; line-height: 20px; }
  .card--front .brand { left: 95px; }
  .card--back .brand { left: 4px; }

  .contact { position: absolute; left: 136px; top: 32px; color: var(--ink); }
  .contact__name { font-size: 14px; color: var(--purple-ink); line-height: 18px; }
  .contact__title { font-size: 6.5px; color: var(--purple-light); margin-top: 4px; }
  .contact__list { list-style: none; margin-top: 17px; }
  .contact__item { position: relative; padding-left: 23px; font-size: 6.5px; line-height: 14px; margin-bottom: 10px; }
  .contact__item svg { position: absolute; left: 3px; top: 1px; width: 12px; height: 12px; }

  .panel .brand { left: 0; width: 424px; top: 90px; }
  .panel .brand__mark { width: 60px; height: 60px; margin-bottom: 46px; }
  .panel .brand__cn { font-size: 15px; line-height: 22px; font-weight: 400; letter-spacing: 2px; }
  .panel .brand__en { font-size: 14px; line-height: 26px; }
</style>
</head>
<body>

<section class="stage-top">
  <div class="card card--front" style="left:120px; top:60px;">
    <div class="card__texture" role="img" aria-label="Faint leaf line pattern in light purple"></div>
    <div class="brand"><span class="brand__mark"></span><span class="brand__cn">岚溪商旅</span><span class="brand__en">Virel Hotel</span></div>
  </div>
  <div class="card card--back" style="left:416px; top:238px;">
    <svg class="card__leaf" viewBox="0 0 312 192" role="img" aria-label="Pale green sweeping shape on the right edge"><path d="M312 0 C270 40 248 120 232 192 L312 192 Z" fill="var(--lime-pale)"/></svg>
    <div class="brand"><span class="brand__mark"></span><span class="brand__cn">岚溪商旅</span><span class="brand__en">Virel Hotel</span></div>
    <div class="contact">
      <p class="contact__name">Lena C. Haworth</p>
      <p class="contact__title">Sales Manager</p>
      <ul class="contact__list">
        <li class="contact__item"><svg viewBox="0 0 12 12" fill="none" stroke="var(--icon)" stroke-width="0.8"><path d="M3 1.5l1.5 2-1 1.2c.6 1.4 1.6 2.4 3 3l1.2-1 2 1.5-1 1.8C5.5 9.8 2.2 6.5 1.8 2.5z"/></svg>270-555-0184</li>
        <li class="contact__item"><svg viewBox="0 0 12 12" fill="none" stroke="var(--icon)" stroke-width="0.8"><rect x="1" y="2.5" width="10" height="7"/><path d="M1 2.5l5 4 5-4"/></svg>lena.haworth@virelhotel.tw</li>
        <li class="contact__item"><svg viewBox="0 0 12 12" fill="none" stroke="var(--icon)" stroke-width="0.8"><path d="M6 11S2.5 7 2.5 4.5a3.5 3.5 0 0 1 7 0C9.5 7 6 11 6 11z"/><circle cx="6" cy="4.5" r="1.2"/></svg>418 Willow Crest Lane<br>Maple Ridge, KY 42750</li>
      </ul>
    </div>
  </div>
</section>

<section class="stage-cards">
  <div class="card card--front" style="left:82px; top:103px;">
    <div class="card__texture" role="img" aria-label="Faint leaf line pattern in light purple"></div>
    <div class="brand"><span class="brand__mark"></span><span class="brand__cn">岚溪商旅</span><span class="brand__en">Virel Hotel</span></div>
  </div>
  <div class="card card--back" style="left:454px; top:103px;">
    <svg class="card__leaf" viewBox="0 0 312 192" role="img" aria-label="Pale green sweeping shape on the right edge"><path d="M312 0 C270 40 248 120 232 192 L312 192 Z" fill="var(--lime-pale)"/></svg>
    <div class="brand"><span class="brand__mark"></span><span class="brand__cn">岚溪商旅</span><span class="brand__en">Virel Hotel</span></div>
    <div class="contact">
      <p class="contact__name">Lena C. Haworth</p>
      <p class="contact__title">Sales Manager</p>
      <ul class="contact__list">
        <li class="contact__item"><svg viewBox="0 0 12 12" fill="none" stroke="var(--icon)" stroke-width="0.8"><path d="M3 1.5l1.5 2-1 1.2c.6 1.4 1.6 2.4 3 3l1.2-1 2 1.5-1 1.8C5.5 9.8 2.2 6.5 1.8 2.5z"/></svg>270-555-0184</li>
        <li class="contact__item"><svg viewBox="0 0 12 12" fill="none" stroke="var(--icon)" stroke-width="0.8"><rect x="1" y="2.5" width="10" height="7"/><path d="M1 2.5l5 4 5-4"/></svg>lena.haworth@virelhotel.tw</li>
        <li class="contact__item"><svg viewBox="0 0 12 12" fill="none" stroke="var(--icon)" stroke-width="0.8"><path d="M6 11S2.5 7 2.5 4.5a3.5 3.5 0 0 1 7 0C9.5 7 6 11 6 11z"/><circle cx="6" cy="4.5" r="1.2"/></svg>418 Willow Crest Lane<br>Maple Ridge, KY 42750</li>
      </ul>
    </div>
  </div>
</section>

<section class="panel panel--light">
  <div class="brand"><span class="brand__mark"></span><span class="brand__cn">岚溪商旅</span><span class="brand__en">Virel Hotel</span></div>
</section>
<section class="panel panel--dark">
  <div class="brand"><span class="brand__mark"></span><span class="brand__cn">岚溪商旅</span><span class="brand__en">Virel Hotel</span></div>
</section>

</body>
</html>
```